Your complete Gardening and lawn maintenance, Horticultural care. (to be on card)
We are looking at using a logo of a tree, with a recycling emblem circling the tree. The colors of choice, are burnt oranges and olive greens. Presented; simple to the eye, yet catchy to the clients in a eco-friendly way. We have uploaded a design for you to look at just to give a rough idea, you can use that or create your own ideas or play around with a mixture.

Target Market(s)

Home owners, businesses, real estates.

Industry/Entity Type

Recycling

Contact Information for Business Card

Name: Colin Breversted
Phone: 0438159027
Email: brightmossyards@mailbarn.net

Logo Text

Bright-Moss Yards

Logo styles of interest
Emblem Logo
Pictorial/Combination Logo
Abstract Logo
Requirements
Must have
• Business name: Bright-Moss Yards
and slogan : Your complete Gardening and lawn maintenance, Horticultural care

```html
<!DOCTYPE html>
<html lang="en">
<head>
<meta charset="utf-8">
<title>Bright-Moss Yards — Business Card</title>
<link rel="stylesheet" href="https://fonts.googleapis.com/css2?family=Cabin:ital,wght@0,400;0,700;1,400;1,700&display=swap">
<style>
  :root {
    --backdrop: #7e3420;
    --card-white: #ffffff;
    --olive: #5b6a29;
    --olive-light: #7d8f3a;
    --leaf-lime: #b3cc3c;
    --ink: #24261a;
    --burnt-orange: #8c3519;
    --white: #ffffff;
  }
  * { margin: 0; padding: 0; box-sizing: border-box; }
  html, body { width: 1200px; height: 684px; overflow: hidden; }
  body {
    background: var(--backdrop);
    font-family: "Cabin", sans-serif;
    position: relative;
  }
  .card {
    position: absolute;
    top: 195px;
    width: 494px;
    height: 281px;
    background: var(--card-white);
    overflow: hidden;
  }
  .card-front { left: 70px; }
  .card-back { left: 636px; }

  /* Front */
  .front-wordmark {
    position: absolute;
    top: 70px;
    left: 0;
    width: 100%;
    display: flex;
    justify-content: center;
    align-items: center;
    gap: 12px;
  }
  .wordmark-dot {
    width: 16px; height: 16px; border-radius: 50%;
    background: var(--olive);
    flex: none;
  }
  .wordmark {
    font-family: "Cabin", sans-serif;
    font-weight: 400;
    color: var(--ink);
    white-space: nowrap;
    letter-spacing: -0.5px;
  }
  .front-wordmark .wordmark { font-size: 44px; }
  .front-band {
    position: absolute;
    left: 0; bottom: 0;
    width: 100%;
    height: 110px;
    background: var(--olive);
  }
  .band-edge-top {
    position: absolute;
    left: 0; top: -10px;
    width: 100%; height: 10px;
    display: block;
  }
  .slogan {
    position: absolute;
    top: 27px; left: 0; width: 100%;
    text-align: center;
    font-style: italic;
    font-size: 18px;
    line-height: 22px;
    color: var(--white);
  }
  .slogan strong { color: var(--leaf-lime); font-weight: 700; }

  /* Back */
  .back-strip {
    position: absolute;
    left: 0; top: 0;
    width: 102px; height: 100%;
    background: var(--olive);
  }
  .band-edge-side {
    position: absolute;
    top: 0; left: 102px;
    width: 10px; height: 100%;
    display: block;
  }
  .back-wordmark {
    position: absolute;
    top: 58px; right: 26px;
    display: flex; align-items: center; gap: 8px;
  }
  .back-wordmark .wordmark { font-size: 28px; }
  .back-wordmark .wordmark-dot { width: 11px; height: 11px; }
  .holder-name {
    position: absolute;
    top: 140px; left: 146px;
    font-size: 22px;
    font-weight: 700;
    font-style: italic;
    color: var(--burnt-orange);
    letter-spacing: 0.5px;
  }
  .contact-list {
    position: absolute;
    top: 183px; left: 138px;
    list-style: none;
  }
  .contact-item {
    display: flex; align-items: center;
    height: 30px;
    font-size: 20px;
    color: var(--ink);
  }
  .contact-icon { width: 22px; height: 18px; margin-right: 16px; flex: none; }
  .contact-item strong { font-weight: 700; }
</style>
</head>
<body>

<section class="card card-front" aria-label="Business card front">
  <div class="front-wordmark">
    <span class="wordmark-dot"></span>
    <span class="wordmark">Bright-Moss Yards</span>
  </div>
  <div class="front-band">
    <svg class="band-edge-top" viewBox="0 0 494 10" preserveAspectRatio="none" aria-hidden="true">
      <defs>
        <pattern id="teeth-up" width="17" height="10" patternUnits="userSpaceOnUse">
          <polygon points="0,10 8.5,0 17,10" fill="#5b6a29"/>
        </pattern>
      </defs>
      <rect width="494" height="10" fill="url(#teeth-up)"/>
    </svg>
    <p class="slogan">Your <strong>complete</strong> gardening and lawn<br>maintenance, horticultural care</p>
  </div>
</section>

<section class="card card-back" aria-label="Business card back">
  <div class="back-strip"></div>
  <svg class="band-edge-side" viewBox="0 0 10 281" preserveAspectRatio="none" aria-hidden="true">
    <defs>
      <pattern id="teeth-side" width="10" height="16" patternUnits="userSpaceOnUse">
        <polygon points="0,0 10,8 0,16" fill="#5b6a29"/>
      </pattern>
    </defs>
    <rect width="10" height="281" fill="url(#teeth-side)"/>
  </svg>

  <div class="back-wordmark">
    <span class="wordmark-dot"></span>
    <span class="wordmark">Bright-Moss Yards</span>
  </div>

  <p class="holder-name">Colin Breversted</p>

  <ul class="contact-list">
    <li class="contact-item">
      <svg class="contact-icon" viewBox="0 0 22 18" aria-hidden="true">
        <path d="M6 1 C4 1 2 3 3 6 C5 11 9 15 14 17 C17 18 19 16 19 14 L15 11 L12.5 13 C10 12 7.5 9.5 6.5 7 L8.5 4.5 Z" fill="#5b6a29"/>
      </svg>
      <span>043 815 9027</span>
    </li>
    <li class="contact-item">
      <svg class="contact-icon" viewBox="0 0 22 18" aria-hidden="true">
        <rect x="1" y="2" width="20" height="14" fill="#5b6a29"/>
        <polyline points="1,2 11,10 21,2" fill="none" stroke="#ffffff" stroke-width="1.5"/>
      </svg>
      <span><strong>brightmoss</strong>yards@mailbarn.net</span>
    </li>
  </ul>
</section>

</body>
</html>
```